Business Card Design

Business Card for professional consulting firm working with large financial institutions.

Target Market(s)

Executive buyers

Industry/Entity Type

Banking

Contact Information for Business Card

Mild creativity wanted. Not boring, but do elaborate artwork.

Font styles to use
Serif
Sans Serif

Colors

Designer to choose colors to be used in the design.

Requirements
Must have
• Standard business card features - company name, individual name, telephone, website, email, locations.
Nice to have
• Two colors
Should not have
• too many colors, fancy printing, cartoons.

```html
<!DOCTYPE html>
<html lang="en">
<head>
<meta charset="utf-8">
<title>Norvane Partners – Business Card</title>
<link href="https://fonts.googleapis.com/css2?family=Lato:wght@300;400;700&display=swap" rel="stylesheet">
<style>
  :root {
    --canvas: #3a3b3d;
    --card-white: #ffffff;
    --card-mist: #efefef;
    --band-grey: #a9a9a9;
    --band-black: #111111;
    --ink: #1c1c1c;
    --ink-soft: #555555;
    --rule: #9a9a9a;
    --map-tone: #e2e2e2;
  }
  * { box-sizing: border-box; margin: 0; padding: 0; }
  html, body { width: 1200px; height: 1200px; overflow: hidden; }
  body {
    background: var(--canvas);
    font-family: 'Lato', sans-serif;
    color: var(--ink);
    position: relative;
  }
  .card {
    position: absolute;
    left: 150px;
    width: 900px;
    height: 514px;
    border-radius: 44px;
    overflow: hidden;
    background: var(--card-white);
    box-shadow: 0 14px 30px rgba(0,0,0,0.35);
  }
  .card--front { top: 50px; }
  .card--back { top: 636px; }
  .card__waves { position: absolute; inset: 0; width: 100%; height: 100%; }

  .world-map {
    position: absolute;
    left: 210px; top: 30px;
    width: 480px; height: 240px;
    border-radius: 50%;
    background: radial-gradient(ellipse at center, var(--map-tone) 0%, rgba(226,226,226,0) 70%);
  }
  .brand {
    position: absolute;
    display: flex; align-items: center; gap: 14px;
    font-family: 'Lato', sans-serif;
    font-weight: 400;
    color: var(--ink);
  }
  .brand__dot {
    width: 22px; height: 22px; border-radius: 50%;
    background: var(--band-grey);
  }
  .card--front .brand {
    left: 0; right: 0; top: 110px; justify-content: center;
    font-size: 52px;
  }
  .tagline {
    position: absolute; left: 0; right: 0; top: 200px;
    text-align: center;
    font-size: 19px; letter-spacing: 1.5px;
    color: var(--ink);
  }

  .identity {
    position: absolute; left: 70px; top: 60px; width: 760px;
  }
  .identity__name {
    font-size: 60px; letter-spacing: 1px; line-height: 1;
    font-weight: 400; color: var(--ink);
  }
  .identity__name .surname { font-weight: 300; color: var(--ink-soft); }
  .identity__title {
    margin-top: 8px; font-size: 22px; letter-spacing: 2.5px;
    color: var(--ink-soft); font-weight: 400;
    padding-bottom: 10px; border-bottom: 2px solid var(--rule);
  }
  .contact {
    position: absolute; left: 300px; top: 175px;
    list-style: none; font-size: 19px; color: var(--ink);
  }
  .contact li { display: flex; align-items: flex-start; gap: 12px; margin-bottom: 8px; line-height: 1.2; }
  .contact li.contact__address { margin-bottom: 20px; }
  .contact svg { width: 20px; height: 20px; flex: none; margin-top: 1px; fill: var(--ink-soft); }
  .card--back .brand {
    left: 70px; bottom: 70px; font-size: 34px;
  }
</style>
</head>
<body>

  <section class="card card--front" aria-label="Card front">
    <svg class="card__waves" viewBox="0 0 900 514" preserveAspectRatio="none" aria-hidden="true">
      <path d="M0,0 H900 V300 C760,350 560,380 420,372 C260,360 120,300 0,250 Z" fill="var(--card-mist)"/>
      <path d="M0,250 C130,300 260,352 420,370 C300,372 150,330 0,290 Z" fill="var(--band-grey)"/>
      <path d="M250,355 C460,390 700,360 900,295 V340 C700,420 470,420 250,355 Z" fill="var(--band-black)"/>
    </svg>
    <div class="world-map" role="img" aria-label="Faint world map background"></div>
    <div class="brand"><span class="brand__dot"></span>Norvane Partners</div>
    <p class="tagline">STRATEGY | ADVISORY | EXECUTION</p>
  </section>

  <section class="card card--back" aria-label="Card back">
    <svg class="card__waves" viewBox="0 0 900 514" preserveAspectRatio="none" aria-hidden="true">
      <path d="M0,0 H900 V300 C760,350 560,380 420,372 C260,360 120,300 0,250 Z" fill="var(--card-mist)"/>
      <path d="M0,250 C130,300 260,352 420,370 C300,372 150,330 0,290 Z" fill="var(--band-grey)"/>
      <path d="M250,355 C460,390 700,360 900,295 V340 C700,420 470,420 250,355 Z" fill="var(--band-black)"/>
    </svg>

    <div class="identity">
      <h1 class="identity__name">DANIEL <span class="surname">HART</span></h1>
      <p class="identity__title">MANAGING DIRECTOR</p>
    </div>

    <ul class="contact">
      <li class="contact__address">
        <svg viewBox="0 0 20 20"><path d="M10 2 L19 10 H16 V18 H12 V13 H8 V18 H4 V10 H1 Z"/></svg>
        <span>40 Harbor Street Meridian Plaza<br>12th Floor Eastport, Ohio 44120</span>
      </li>
      <li>
        <svg viewBox="0 0 20 20"><path d="M2 8 C2 4 18 4 18 8 V10 H14 V8 H6 V10 H2 Z M5 11 H15 L17 17 H3 Z"/></svg>
        <span>555-014-2290</span>
      </li>
      <li>
        <svg viewBox="0 0 20 20"><path d="M1 4 H19 V16 H1 Z M2 5 L10 11 L18 5" stroke="#fff" stroke-width="1.2"/></svg>
        <span>info@norvanepartners.com</span>
      </li>
      <li>
        <svg viewBox="0 0 20 20"><circle cx="10" cy="10" r="9"/><path d="M1 10 H19 M10 1 V19 M4 5 H16 M4 15 H16" stroke="#fff" stroke-width="1"/></svg>
        <span>www.norvanepartners.com</span>
      </li>
    </ul>

    <div class="brand"><span class="brand__dot"></span>Norvane Partners</div>
  </section>

</body>
</html>
```